TR Advisory Business Cards - High End AV / Low Voltage Company

We are low voltage AV company that specializes in high end clients on the residential side and larger businesses on the commercial side. We want something modern, tech looking but also something that is extremely professional looking. We have uploaded our logos and postcards we already have in the field. Along with a picture of one of our wrapped vans. Our website is at www.trvadvisory.example and our primary colors are the orange, green, grey and blue all military color finishes.

We are interesting in the slogans "Pairing You with the Right Technology" or "Bringing the Coast Modern Tech"

Target Market(s)

We focus on 70% Commercial and 30% Residential Customers

Industry/Entity Type

Low Voltage, AV Company

Contact Information for Business Card

Name - Dorian Fairweather, Title - Owner, Office Phone - 555-714-3096, Mobile Phone - 555-802-4173, E-Mail - d@trvadvisory.example, Website: www.trvadvisory.example

Font styles to use
Sans Serif

Requirements
Must have
• Must have Name, Title, Work Phone & Mobile, Website and Logo.
Nice to have
• We want something that will impress our higher end clients with a great logo
Should not have
• Too traditional or plain.

```html
<!DOCTYPE html>
<html lang="en">
<head>
<meta charset="utf-8">
<title>TR Advisory – Business Card</title>
<link href="https://fonts.googleapis.com/css2?family=Montserrat:wght@400;500;600;700&display=swap" rel="stylesheet">
<style>
  :root {
    --backdrop: #e4e5e3;
    --card: #f1f1f1;
    --orange: #e0643a;
    --ink: #2b2b2b;
    --band: #232a1c;
    --band-text: #ecece6;
  }
  * { box-sizing: border-box; margin: 0; padding: 0; }
  html, body {
    width: 1200px; height: 1200px; overflow: hidden;
    background: var(--backdrop);
    font-family: "Montserrat", sans-serif;
  }
  .stage { position: relative; width: 1200px; height: 1200px; }
  .card {
    position: absolute; top: 216px; width: 416px; height: 728px;
    background: var(--card);
    border-radius: 4px;
    box-shadow: 0 10px 24px rgba(0,0,0,0.18);
    overflow: hidden;
  }
  .card--front { left: 134px; }
  .card--back { left: 611px; }

  .brand {
    position: absolute; left: 0; right: 0;
    display: flex; align-items: center; justify-content: center; gap: 10px;
    color: var(--orange); font-weight: 600; line-height: 1;
  }
  .card--front .brand { top: 140px; font-size: 36px; }
  .card--back .brand { top: 340px; font-size: 42px; }
  .brand__dot {
    width: 18px; height: 18px; border-radius: 50%;
    border: 3px solid var(--orange);
  }

  .circuit-texture {
    position: absolute; left: 90px; top: 250px; width: 326px; height: 403px;
    background: radial-gradient(ellipse at 80% 45%, rgba(0,0,0,0.035), rgba(0,0,0,0) 70%);
  }

  .person { position: absolute; left: 0; right: 0; top: 309px; text-align: center; }
  .person__name { color: var(--orange); font-weight: 700; font-size: 25px; line-height: 30px; }
  .person__title { color: var(--ink); font-weight: 400; font-size: 18px; line-height: 22px; }

  .contact-icons {
    position: absolute; left: 0; right: 0; top: 440px;
    display: flex; justify-content: center; gap: 9px;
  }
  .contact-icons svg { width: 17px; height: 19px; fill: var(--orange); }

  .contact { position: absolute; left: 0; right: 0; top: 468px; text-align: center; list-style: none; }
  .contact li { color: var(--ink); font-size: 18.5px; line-height: 30.5px; font-weight: 400; }

  .tagline-band {
    position: absolute; left: 0; right: 0; bottom: 0; height: 75px;
    background: var(--band);
    display: flex; align-items: center; justify-content: center;
    color: var(--band-text); font-size: 18.5px; font-weight: 400; letter-spacing: 0.2px;
  }
</style>
</head>
<body>
<main class="stage">
  <section class="card card--front">
    <div class="circuit-texture" role="img" aria-label="Faint circuit-trace pattern in light grey"></div>
    <div class="brand"><span class="brand__dot"></span><span>TR Advisory</span></div>
    <div class="person">
      <p class="person__name">Dorian Fairweather</p>
      <p class="person__title">Owner</p>
    </div>
    <div class="contact-icons" aria-hidden="true">
      <svg viewBox="0 0 20 20"><path d="M5 2l3 4-2 2c1 2 3 4 5 5l2-2 4 3-2 3C9 17 3 11 3 4z"/></svg>
      <svg viewBox="0 0 20 20"><path d="M6 1h8a1 1 0 0 1 1 1v16a1 1 0 0 1-1 1H6a1 1 0 0 1-1-1V2a1 1 0 0 1 1-1zm1 2v12h6V3zm3 13a1 1 0 1 0 0 2 1 1 0 0 0 0-2z"/></svg>
      <svg viewBox="0 0 20 20"><path d="M2 5h16v1l-8 5-8-5zm0 3l8 5 8-5v8H2z"/></svg>
      <svg viewBox="0 0 20 20"><path d="M10 2a8 8 0 1 0 0 16 8 8 0 0 0 0-16zm-1 2c-1 2-3 2-3 4s3 1 3 3-1 3 0 5a6 6 0 0 1 0-12zm3 1c2 1 3 3 3 5-1 0-2-1-3 0s1 3-1 4c0-2-2-2-2-4s3-2 3-5z"/></svg>
    </div>
    <ul class="contact">
      <li>555-714-3096</li>
      <li>555-802-4173</li>
      <li>d@trvadvisory.example</li>
      <li>www.trvadvisory.example</li>
    </ul>
    <div class="tagline-band">Bringing the Coast Modern Tech</div>
  </section>

  <section class="card card--back">
    <div class="brand"><span class="brand__dot"></span><span>TR Advisory</span></div>
  </section>
</main>
</body>
</html>
```